Need Modern Elegant Professional Invoice Design

Need modern elegant professional invoice design along with a second page for time and expense log for professional services

```html
<!DOCTYPE html>
<html lang="en">
<head>
<meta charset="UTF-8">
<title>Invoice – Keystone Adjusters</title>
<link href="https://fonts.googleapis.com/css2?family=Roboto:wght@400;500&display=swap" rel="stylesheet">
<style>
:root{
  --orange:#ec7f22;
  --navy:#3a2f8f;
  --ink:#111111;
  --text:#555555;
  --muted:#d4d4d8;
  --row-cool:#eff0f6;
  --row-warm:#fbf1e9;
  --rule:#222222;
  --paper:#ffffff;
}
*{margin:0;padding:0;box-sizing:border-box}
html,body{width:848px;height:1200px;overflow:hidden;background:var(--paper)}
body{font-family:'Roboto',Arial,sans-serif;color:var(--text);font-size:12px;position:relative}
.sheet{position:absolute;inset:0;border:1px solid #2b2b2b}
.abs{position:absolute}
.label{font-weight:500;color:var(--ink);letter-spacing:4.2px;font-size:12px;text-transform:uppercase}
.value{font-size:12px;line-height:17px}

.brand{left:101px;top:112px;display:flex;align-items:center;gap:10px}
.brand-dot{width:22px;height:22px;border-radius:50%;background:var(--navy)}
.brand-name{font-size:34px;font-weight:500;color:var(--orange);letter-spacing:2px}

.company{left:545px;top:108px}
.company .label{margin-bottom:3px}

.doc-title{left:0;width:790px;text-align:center;top:276px;font-size:21px;font-weight:500;color:var(--ink);letter-spacing:8px}

.meta{left:545px}
.meta .value{margin-top:3px}

.to{left:101px;top:404px}
.to-tag{font-size:12px;letter-spacing:4px;color:var(--text)}
.to-block{left:141px;top:406px}

.invoice-no{left:350px;top:404px}
.invoice-no .value{margin-top:3px}

.items{left:102px;top:479px;width:665px;border-collapse:collapse}
.items th{background:var(--orange);color:#fff;font-weight:500;font-size:11.5px;letter-spacing:4.2px;text-align:left;vertical-align:top;padding:10px 5px 0;height:41px;border-right:2px solid #fff}
.items th:last-child{border-right:none}
.items th.num,.items td.num{text-align:center}
.items th.amt{text-align:center}
.items td{font-size:12px;line-height:17px;vertical-align:top;padding:16px 5px 0;border-bottom:1px solid var(--rule);color:var(--text)}
.items td.item{color:var(--ink)}
.items td.amt{text-align:right;padding-right:14px;color:var(--ink);letter-spacing:4px;font-size:12.5px}
.items tr.cool td{background:var(--row-cool)}
.items tr.warm td{background:var(--row-warm)}
.items td.desc{padding-right:6px;text-align:justify}

.totals .label{right:294px;text-align:right}
.total-box{left:659px;top:772px;width:108px;height:29px;border:1px solid var(--rule);background:#f6f1f4;color:var(--ink);font-size:12.5px;letter-spacing:4px;text-align:right;padding:9px 13px 0 0}

.pay{left:101px;top:900px}
.pay h3,.tax h3{font-size:12.5px;font-weight:500;color:var(--ink);line-height:17px}
.tax{left:101px;top:986px}

.sign{left:559px;top:897px}
.date-hint{margin-top:2px;color:var(--muted);letter-spacing:6px;font-size:12px;padding-left:3px}
.sign-label{left:559px;top:982px}

.terms{left:101px;top:1083px}
.terms .value{margin-top:3px}
</style>
</head>
<body>
<div class="sheet">

  <div class="abs brand">
    <span class="brand-dot"></span>
    <span class="brand-name">KEYSTONE</span>
  </div>

  <div class="abs company">
    <div class="label">Keystone Adjusters</div>
    <div class="value">PO Box 218, Maple Ridge,<br>NY 12110<br>Telephone: 518-555-0142<br>Fax: 888-555-0178<br>www.keystoneadjusters.com<br>Email. office@keystoneadjusters.com</div>
  </div>

  <div class="abs doc-title">INVOICE</div>

  <div class="abs meta" style="top:306px">
    <div class="label">Client Claim Number</div>
    <div class="value">12345678</div>
  </div>
  <div class="abs meta" style="top:355px">
    <div class="label">Insured Name</div>
    <div class="value">JOHN DOE</div>
  </div>
  <div class="abs meta" style="top:403px">
    <div class="label">Policy Number</div>
    <div class="value">1234567890</div>
  </div>

  <div class="abs to"><span class="to-tag">TO :</span></div>
  <div class="abs to-block">
    <div class="label">John Doe</div>
    <div class="value" style="margin-top:3px">412 Cedar Lane, Maple Ridge,<br>New York 12110</div>
  </div>

  <div class="abs invoice-no">
    <div class="label">Invoice</div>
    <div class="value">DSN12 / 121 / 16816</div>
  </div>

  <table class="abs items">
    <colgroup>
      <col style="width:55px"><col style="width:90px"><col style="width:312px"><col style="width:100px"><col style="width:108px">
    </colgroup>
    <thead>
      <tr><th>Item No.</th><th>Date</th><th>Description</th><th class="num">Hours</th><th class="amt">Amount</th></tr>
    </thead>
    <tbody>
      <tr class="cool" style="height:59px"><td class="item">1</td><td>04/19/2021</td><td class="desc">Lorem ipsum dolor sit amet, consectetur adipiscing elit, sed do eiusmod tempor incididunt ut labore.</td><td class="num">10</td><td class="amt">$ 100.00</td></tr>
      <tr class="warm" style="height:41px"><td class="item">2</td><td>04/19/2021</td><td class="desc">Praesent tristique consectetur</td><td class="num">20</td><td class="amt">$ 250.00</td></tr>
      <tr class="cool" style="height:58px"><td class="item">3</td><td>04/19/2021</td><td class="desc">Nunc quis tortor a mi fringilla molestie sed varius turpis. In sollicitudin pellentesque lectus, ut imperdiet neque.</td><td class="num">30</td><td class="amt">$ 90.00</td></tr>
      <tr class="warm" style="height:59px"><td class="item">4</td><td>04/19/2021</td><td class="desc">Ut ac nisi convallis arcu facilisis bibendum. Pellentesque varius arcu ligula, quis rutrum quam eleifend ac.</td><td class="num">40</td><td class="amt">$ 300.00</td></tr>
    </tbody>
  </table>

  <div class="totals">
    <div class="abs label" style="top:780px">Total Hours</div>
    <div class="abs label" style="top:814px">Mileage</div>
    <div class="abs label" style="top:839px">Expenses</div>
  </div>
  <div class="abs total-box">$ 840.00</div>

  <div class="abs pay">
    <h3>Payment Method</h3>
    <div class="value">Bank details<br>Acount Holder : KEYSTONE<br>Acount No : 222 444 666 888</div>
  </div>

  <div class="abs tax">
    <h3>Tax ID Number</h3>
    <div class="value">27-4405186</div>
  </div>

  <div class="abs sign">
    <div class="value">your place,</div>
    <div class="date-hint">mm <span style="color:var(--ink)">/</span> dd <span style="color:var(--ink)">/</span> yyyy</div>
  </div>
  <div class="abs sign-label value">Signature</div>

  <div class="abs terms">
    <div class="label">Payment Terms</div>
    <div class="value">Nulla ac aliquam elit. Nunc quis tortor a mi fringilla molestie sed varius turpis.</div>
  </div>

</div>
</body>
</html>
```